Medical program Ombo produce by VALORENZA

I need a business card of the program to give to the customer to get the general information to contact the clinic. I need a bilingual card French and English you will see the logo.
That's a program that the Clinic Valorenza offers. https://medicalombo.ca
Program: Ombo Medical Program
Slogan: Lose weight - Exist - Live / Be thin - Exist - Live
The clinic that offers the program: Valorenza
Website: https://medicalombo.ca
---
Medical team / Medical team
email: doc@valorenza.ca
phone: 514 555-0147
Information
email: ombo@valorenza.ca
phone: 514 555-0183 ext 3
Target Market(s)
Every person that needs to lose weight
Industry/Entity Type
Health clinic for obese person
Contact Information for Business Card
All the information in the description
Requirements
Must have
- Look clean - Expensive clinic / Need to be bilingual
Nice to have
- Recto verso for french and english
Should not have
- -

```html
<!DOCTYPE html>
<html lang="fr">
<head>
<meta charset="utf-8">
<title>Ombo Medical Program – Business Cards</title>
<link href="https://fonts.googleapis.com/css2?family=Poppins:wght@400;500;600;700&display=swap" rel="stylesheet">
<style>
  :root {
    --backdrop: #30ada3;
    --card: #ffffff;
    --ink: #1d1d1b;
    --red: #e0252f;
    --teal: #14a39a;
    --grey: #3b3a39;
  }
  * { box-sizing: border-box; margin: 0; padding: 0; }
  html, body {
    width: 1200px; height: 960px; overflow: hidden;
    background: var(--backdrop);
    font-family: "Poppins", sans-serif;
  }
  .card {
    position: absolute; left: 323px; width: 553px; height: 332px;
    background: var(--card);
  }
  .card--fr { top: 113px; --accent: var(--red); }
  .card--en { top: 519px; --accent: var(--teal); }

  .program-name {
    position: absolute; left: 42px; top: 70px;
    font-size: 27px; font-weight: 500; line-height: 1;
    color: var(--teal); letter-spacing: .5px;
  }

  .clinic {
    position: absolute; left: 313px; top: 78px;
    display: flex; align-items: center; gap: 10px;
  }
  .clinic__mark { width: 30px; height: 30px; background: var(--red); }
  .clinic__name { font-size: 23px; font-weight: 700; color: var(--grey); letter-spacing: .3px; line-height: 1; }

  .contact { position: absolute; left: 42px; }
  .contact--info { top: 163px; }
  .contact--team { top: 256px; }
  .contact__title {
    font-size: 14.5px; font-weight: 700; color: var(--accent);
    margin-bottom: 3px; letter-spacing: .2px;
  }
  .contact__line {
    display: flex; align-items: center; gap: 13px;
    font-size: 12.5px; font-weight: 600; color: var(--ink); height: 16.5px;
  }
  .contact__line svg { width: 14px; height: 14px; flex: none; }
  .icon { fill: var(--accent); stroke: var(--accent); }
</style>
</head>
<body>

<svg width="0" height="0" style="position:absolute">
  <defs>
    <symbol id="icon-mail" viewBox="0 0 16 12">
      <rect x="0" y="0" width="16" height="12" rx="1" stroke="none"/>
      <path d="M1 1 L8 7 L15 1" fill="none" stroke="#fff" stroke-width="1.3"/>
    </symbol>
    <symbol id="icon-phone" viewBox="0 0 16 16">
      <path stroke="none" d="M3.5 1 L6 1 L7 4.5 L5.3 6 C6.2 8 8 9.8 10 10.7 L11.5 9 L15 10 L15 12.5 C15 13.8 14 15 12.5 15 C6.5 14.5 1.5 9.5 1 3.5 C1 2 2 1 3.5 1 Z"/>
    </symbol>
    <symbol id="icon-globe" viewBox="0 0 16 16">
      <g fill="none" stroke-width="1.3">
        <circle cx="8" cy="8" r="6.8"/>
        <ellipse cx="8" cy="8" rx="3" ry="6.8"/>
        <path d="M1.2 8 H14.8 M2.3 4.5 H13.7 M2.3 11.5 H13.7"/>
      </g>
    </symbol>
  </defs>
</svg>

<section class="card card--fr" lang="fr">
  <div class="program-name">Medical Ombo</div>
  <div class="clinic">
    <div class="clinic__mark"></div>
    <div class="clinic__name">VALORENZA</div>
  </div>
  <div class="contact contact--info">
    <h2 class="contact__title">POUR INFORMATION</h2>
    <p class="contact__line"><svg class="icon"><use href="#icon-mail"/></svg>OMBO@VALORENZA.CA</p>
    <p class="contact__line"><svg class="icon"><use href="#icon-phone"/></svg>514 555-0183 EXT 3</p>
    <p class="contact__line"><svg class="icon"><use href="#icon-globe"/></svg>https://medicalombo.ca</p>
  </div>
  <div class="contact contact--team">
    <h2 class="contact__title">ÉQUIPE MÉDICALE</h2>
    <p class="contact__line"><svg class="icon"><use href="#icon-mail"/></svg>DOC@VALORENZA.CA</p>
    <p class="contact__line"><svg class="icon"><use href="#icon-phone"/></svg>514 555-0147</p>
  </div>
</section>

<section class="card card--en" lang="en">
  <div class="program-name">Medical Ombo</div>
  <div class="clinic">
    <div class="clinic__mark"></div>
    <div class="clinic__name">VALORENZA</div>
  </div>
  <div class="contact contact--info">
    <h2 class="contact__title">FOR INFORMATION</h2>
    <p class="contact__line"><svg class="icon"><use href="#icon-mail"/></svg>OMBO@VALORENZA.CA</p>
    <p class="contact__line"><svg class="icon"><use href="#icon-phone"/></svg>514 555-0183 EXT 3</p>
    <p class="contact__line"><svg class="icon"><use href="#icon-globe"/></svg>https://medicalombo.ca</p>
  </div>
  <div class="contact contact--team">
    <h2 class="contact__title">MEDICAL TEAM</h2>
    <p class="contact__line"><svg class="icon"><use href="#icon-mail"/></svg>DOC@VALORENZA.CA</p>
    <p class="contact__line"><svg class="icon"><use href="#icon-phone"/></svg>514 555-0147</p>
  </div>
</section>

</body>
</html>
```